Business Card and Stationary for sales
Industrial and Oilfield Supply Company
Business Card and Stationary for sales - Industrial Supplies
Creative Brief
Modern
Marcus Palmer
4381 North Brevard Ave.
marc@palmerdepot.net
www.palmerdepot.net
WE are wanting graphics on the front based around our logo. The colors should be pulled from the logo as well.
Use the information for front side
authorized Vexlor distributor
Crown To Heel Guard Stationary
Rodrigue Teklu
Business Staionary
Time is a factor, contest will end when a draft is up that we like.

```html
<!DOCTYPE html>
<html lang="en">
<head>
<meta charset="utf-8">
<title>Palmer Depot — Stationery Set</title>
<link href="https://fonts.googleapis.com/css2?family=Michroma&family=Encode+Sans+Condensed:wght@400;600&family=Tinos&display=swap" rel="stylesheet">
<style>
:root{
  --bg:#8e8e8e;
  --bg-dark:#6f6f6f;
  --red:#b3121b;
  --red-deep:#6d0a10;
  --red-bright:#d8202a;
  --ink:#3c3c3c;
  --paper:#ffffff;
  --paper-shade:#ececec;
  --charcoal:#2b2b2b;
  --label:#1c1c1c;
}
*{margin:0;padding:0;box-sizing:border-box}
html,body{width:1200px;height:263px;overflow:hidden}
body{background:radial-gradient(ellipse at 50% 40%,var(--bg) 0%,var(--bg-dark) 100%);position:relative;font-family:"Encode Sans Condensed",sans-serif;color:var(--ink)}
.piece{position:absolute;box-shadow:0 1px 3px rgba(0,0,0,.35)}
.label{position:absolute;font-family:"Tinos",serif;font-size:4px;color:var(--label);text-align:center;transform:translateX(-50%);white-space:nowrap}
.brand{font-family:"Michroma",sans-serif;color:var(--red);letter-spacing:.02em;white-space:nowrap;line-height:1}
.brand-mark{display:inline-block;background:var(--red);border-radius:50%;vertical-align:middle}
.tagline{font-size:2px;color:var(--ink);white-space:nowrap}
.name{color:var(--red);font-size:3.4px;font-weight:600;white-space:nowrap}
.contact{font-size:2.4px;line-height:1.45;white-space:nowrap;color:var(--ink)}
.contact .ico{display:inline-block;width:1.6px;height:1.6px;border-radius:50%;background:var(--red);margin-right:1px;vertical-align:middle}
.divider{position:absolute;width:.3px;background:#c9c9c9}
.band{position:absolute;left:0;right:0;bottom:0;background:linear-gradient(#d11e27,var(--red-deep));border-top:.6px solid #fff;outline:.4px solid #bbb}
.art{position:absolute;background:linear-gradient(90deg,rgba(200,200,200,.35),rgba(170,170,170,.25));border-radius:2px}
.card-white{background:linear-gradient(#fff,var(--paper-shade))}
.card-red{background:radial-gradient(ellipse at 60% 40%,var(--red-bright),var(--red-deep));border-radius:4px}
.card-red .brand{color:#fff}
</style>
</head>
<body>

<!-- Business card front -->
<div class="piece card-white" style="left:14px;top:50px;width:101px;height:56px;border-radius:3px;overflow:hidden">
  <div style="position:absolute;left:8px;top:21px"><span class="brand-mark" style="width:4px;height:4px;margin-right:1.5px"></span><span class="brand" style="font-size:4.2px">PALMER DEPOT</span></div>
  <div class="tagline" style="position:absolute;left:14px;top:28px">Oilfield • Plumbing • Industrial</div>
  <div class="divider" style="left:58px;top:10px;height:36px"></div>
  <div style="position:absolute;left:64px;top:12px">
    <div class="name">Marcus Palmer</div>
    <div class="contact" style="margin-top:2px">2207 West Route 18</div>
    <div class="contact" style="margin-top:1px"><span class="ico"></span>555-304-1187<br><span class="ico"></span>555-304-2290<br><span class="ico"></span>555-304-3362<br><span class="ico"></span>marc@palmerdepot.net<br><span class="ico"></span>www.palmerdepot.net</div>
  </div>
  <div class="band" style="height:3.5px"></div>
</div>
<div class="label" style="left:62px;top:111px">Front Card</div>

<!-- Business card back option 01 -->
<div class="piece card-red" style="left:14px;top:121px;width:101px;height:57px">
  <div style="position:absolute;left:0;right:0;top:22px;text-align:center"><span class="brand" style="font-size:8.5px">PALMER</span></div>
  <div style="position:absolute;left:0;right:0;top:31px;text-align:center;color:#fff;font-size:2.6px;letter-spacing:2.2px">DEPOT</div>
  <div style="position:absolute;left:0;right:0;top:35px;text-align:center;color:#fff;font-size:2px">Oilfield • Plumbing • Industrial</div>
  <div style="position:absolute;left:0;right:0;top:48px;text-align:center;color:#fff;font-size:2.8px;letter-spacing:.8px">1-800-555-0147</div>
</div>
<div class="label" style="left:62px;top:182px">Back Card Option_01</div>

<!-- Business card back option 02 -->
<div class="piece card-red" style="left:14px;top:192px;width:101px;height:57px">
  <div style="position:absolute;left:0;right:0;top:20px;text-align:center"><span class="brand" style="font-size:8.5px">PALMER</span></div>
  <div style="position:absolute;left:0;right:0;top:29px;text-align:center;color:#fff;font-size:2.6px;letter-spacing:2.2px">DEPOT</div>
  <div style="position:absolute;left:0;right:0;top:33px;text-align:center;color:#fff;font-size:2px">Oilfield • Plumbing • Industrial</div>
  <div style="position:absolute;left:0;right:0;top:47px;text-align:center;color:#fff;font-size:3.2px;font-weight:600;letter-spacing:1px">1-800-555-0147</div>
</div>
<div class="label" style="left:62px;top:253px">Back Card Option_02</div>

<!-- Letterhead option 01 -->
<div class="piece" style="left:122px;top:12px;width:168px;height:238px;background:linear-gradient(#fff,#f3f3f3)">
  <div style="position:absolute;left:5px;top:9px"><span class="brand-mark" style="width:4px;height:4px;margin-right:1.5px"></span><span class="brand" style="font-size:4.2px">PALMER DEPOT</span></div>
  <div class="tagline" style="position:absolute;left:11px;top:16px">Oilfield • Plumbing • Industrial</div>
  <div class="contact" style="position:absolute;left:136px;top:7px">2207 West Route 18<br><span class="ico"></span>555-304-1187<br><span class="ico"></span>555-304-2290<br><span class="ico"></span>555-304-3362<br><span class="ico"></span>marc@palmerdepot.net</div>
  <div class="art" role="img" aria-label="Faint stack of steel pipes with two small standing figures" style="left:18px;top:101px;width:137px;height:41px"></div>
  <div class="band" style="height:8px;display:flex;align-items:center;justify-content:center;color:#fff;font-size:2.6px;letter-spacing:.5px">www.palmerdepot.net</div>
</div>
<div class="label" style="left:206px;top:253px">Letterhead option_01</div>

<!-- Letterhead option 02 -->
<div class="piece" style="left:300px;top:12px;width:168px;height:238px;background:linear-gradient(#fff,#f3f3f3)">
  <div style="position:absolute;left:0;right:0;top:10px;text-align:center"><span class="brand-mark" style="width:4px;height:4px;margin-right:1.5px"></span><span class="brand" style="font-size:4.2px">PALMER DEPOT</span></div>
  <div class="tagline" style="position:absolute;left:0;right:0;top:17px;text-align:center">Oilfield • Plumbing • Industrial</div>
  <div class="art" role="img" aria-label="Faint stack of steel pipes with two small standing figures" style="left:17px;top:101px;width:139px;height:41px"></div>
  <div class="band" style="height:10px;display:flex;align-items:center;justify-content:center;color:#fff;font-size:2.1px;white-space:nowrap">2207 West Route 18 &nbsp; P: 555-304-1187 C: 555-304-2290 F: 555-304-3362 E: marc@palmerdepot.net W: www.palmerdepot.net</div>
</div>
<div class="label" style="left:384px;top:253px">Letterhead option_02</div>

<!-- Email signature 02 -->
<div class="piece card-white" style="left:479px;top:47px;width:111px;height:54px">
  <div style="position:absolute;left:14px;top:22px"><span class="brand-mark" style="width:3.6px;height:3.6px;margin-right:1.2px"></span><span class="brand" style="font-size:3.8px">PALMER DEPOT</span></div>
  <div class="tagline" style="position:absolute;left:19px;top:28px">Oilfield • Plumbing • Industrial</div>
  <div class="divider" style="left:64px;top:6px;height:38px"></div>
  <div style="position:absolute;left:69px;top:8px">
    <div class="name">Marcus Palmer</div>
    <div class="contact" style="margin-top:3px">2207 West Route 18</div>
    <div class="contact" style="margin-top:1px"><span class="ico"></span>555-304-1187<br><span class="ico"></span>555-304-2290<br><span class="ico"></span>555-304-3362<br><span class="ico"></span>marc@palmerdepot.net<br><span class="ico"></span>www.palmerdepot.net</div>
  </div>
  <div class="band" style="height:4px"></div>
</div>
<div class="label" style="left:527px;top:103px">Email Signature_02</div>

<!-- Email signature 03 -->
<div class="piece card-white" style="left:600px;top:27px;width:59px;height:75px">
  <div style="position:absolute;left:0;right:0;top:10px;text-align:center"><span class="brand" style="font-size:3.6px">PALMER DEPOT</span></div>
  <div class="tagline" style="position:absolute;left:0;right:0;top:15px;text-align:center">Oilfield • Plumbing • Industrial</div>
  <div style="position:absolute;left:11px;top:28px">
    <div class="name">Marcus Palmer</div>
    <div class="contact" style="margin-top:3px">2207 West Route 18</div>
    <div class="contact" style="margin-top:1px"><span class="ico"></span>555-304-1187<br><span class="ico"></span>555-304-2290<br><span class="ico"></span>555-304-3362<br><span class="ico"></span>marc@palmerdepot.net<br><span class="ico"></span>www.palmerdepot.net</div>
  </div>
  <div class="band" style="height:4px"></div>
</div>
<div class="label" style="left:630px;top:105px">Email Signature_03</div>

<!-- Email signature 01 -->
<div class="piece card-white" style="left:495px;top:113px;width:144px;height:44px">
  <div style="position:absolute;left:13px;top:14px"><span class="brand-mark" style="width:3.6px;height:3.6px;margin-right:1.2px"></span><span class="brand" style="font-size:3.8px">PALMER DEPOT</span></div>
  <div class="tagline" style="position:absolute;left:18px;top:20px">Oilfield • Plumbing • Industrial</div>
  <div class="divider" style="left:59px;top:6px;height:30px"></div>
  <div style="position:absolute;left:67px;top:16px"><div class="name">Marcus Palmer</div><div class="contact" style="margin-top:2px">2207 West Route 18</div></div>
  <div class="divider" style="left:101px;top:6px;height:30px"></div>
  <div class="contact" style="position:absolute;left:107px;top:11px"><span class="ico"></span>555-304-1187<br><span class="ico"></span>555-304-2290<br><span class="ico"></span>555-304-3362<br><span class="ico"></span>marc@palmerdepot.net<br><span class="ico"></span>www.palmerdepot.net</div>
  <div class="band" style="height:4px"></div>
</div>
<div class="label" style="left:567px;top:161px">Email Signature_01</div>

<!-- Envelope front -->
<div class="piece card-white" style="left:478px;top:171px;width:184px;height:79px">
  <div style="position:absolute;left:5px;top:6px"><span class="brand-mark" style="width:3.6px;height:3.6px;margin-right:1.2px"></span><span class="brand" style="font-size:3.8px">PALMER DEPOT</span></div>
  <div class="tagline" style="position:absolute;left:10px;top:12px">Oilfield • Plumbing • Industrial</div>
  <div class="contact" style="position:absolute;left:17px;top:28px">2207 West Route 18</div>
  <div class="art" role="img" aria-label="Faint stack of steel pipes with two small standing figures" style="left:78px;top:31px;width:98px;height:26px"></div>
  <div class="band" style="height:4px"></div>
</div>
<div class="label" style="left:562px;top:253px">Envelope  Front</div>

<!-- Envelope back (three flap styles) -->
<svg class="piece-set" style="position:absolute;left:671px;top:80px" width="220" height="170" viewBox="0 0 220 170" aria-label="Envelope back flap variations">
  <defs>
    <linearGradient id="flap-red" x1="0" y1="0" x2="0" y2="1"><stop offset="0" stop-color="#d8202a"/><stop offset="1" stop-color="#6d0a10"/></linearGradient>
    <linearGradient id="flap-dark" x1="0" y1="0" x2="0" y2="1"><stop offset="0" stop-color="#444"/><stop offset="1" stop-color="#1c1c1c"/></linearGradient>
    <linearGradient id="flap-white" x1="0" y1="0" x2="0" y2="1"><stop offset="0" stop-color="#fff"/><stop offset="1" stop-color="#e6e6e6"/></linearGradient>
  </defs>
  <!-- dark -->
  <rect x="4" y="0" width="184" height="79" fill="#f4f4f4"/>
  <path d="M4 0 H188 V10 Q96 42 4 10 Z" fill="url(#flap-dark)"/>
  <text x="96" y="23" fill="#fff" font-family="Encode Sans Condensed, sans-serif" font-size="2.5" text-anchor="middle" letter-spacing=".4">www.palmerdepot.net</text>
  <!-- red -->
  <rect x="24" y="43" width="184" height="80" fill="#f7f7f7"/>
  <path d="M24 43 H208 V52 Q116 86 24 52 Z" fill="url(#flap-red)"/>
  <text x="116" y="67" fill="#fff" font-family="Encode Sans Condensed, sans-serif" font-size="2.5" text-anchor="middle" letter-spacing=".4">www.palmerdepot.net</text>
  <!-- white -->
  <rect x="0" y="89" width="184" height="80" fill="url(#flap-white)"/>
  <path d="M0 89 H184 V98 Q92 132 0 98 Z" fill="#fff" stroke="#cfcfcf" stroke-width=".4"/>
  <path d="M0 169 L70 125 M184 169 L114 125" stroke="#d6d6d6" stroke-width=".4"/>
  <text x="92" y="113" fill="#444" font-family="Encode Sans Condensed, sans-serif" font-size="2.5" text-anchor="middle" letter-spacing=".4">www.palmerdepot.net</text>
</svg>
<div class="label" style="left:761px;top:253px">Envelope  Back</div>

<!-- Folder -->
<svg style="position:absolute;left:892px;top:12px" width="292" height="238" viewBox="0 0 292 238" aria-label="Presentation folder, open">
  <defs>
    <linearGradient id="folder-red" x1="0" y1="0" x2="1" y2="1"><stop offset="0" stop-color="#c5141e"/><stop offset="1" stop-color="#6d0a10"/></linearGradient>
    <linearGradient id="pocket-red" x1="0" y1="0" x2="0" y2="1"><stop offset="0" stop-color="#a30f18"/><stop offset="1" stop-color="#c8161f"/></linearGradient>
  </defs>
  <rect x="13" y="0" width="131" height="179" fill="url(#folder-red)"/>
  <rect x="144" y="0" width="135" height="179" fill="#fff"/>
  <path d="M0 125 L13 119 V238 H0 Z" fill="#a30f18"/>
  <path d="M292 125 L279 119 V238 H292 Z" fill="#a30f18"/>
  <path d="M13 179 H144 V238 H13 Z" fill="url(#pocket-red)"/>
  <path d="M144 179 H279 V238 H154 Q146 210 144 179 Z" fill="url(#pocket-red)"/>
  <line x1="13" y1="179" x2="279" y2="179" stroke="#fff" stroke-width=".5" stroke-dasharray="1.5 1"/>
  <line x1="144" y1="0" x2="144" y2="179" stroke="#fff" stroke-width=".5" stroke-dasharray="1.5 1"/>
  <rect role="img" aria-label="Faint stack of steel pipes with two standing figures" x="22" y="78" width="108" height="40" rx="2" fill="#ffffff" fill-opacity=".07"/>
  <g font-family="Encode Sans Condensed, sans-serif" font-size="2.3" fill="#fff">
    <text x="19" y="152">2207 West Route 18</text>
    <text x="20" y="158">● 555-304-1187</text>
    <text x="20" y="162">● 555-304-2290</text>
    <text x="20" y="166">● 555-304-3362</text>
    <text x="20" y="170">● marc@palmerdepot.net</text>
    <text x="20" y="174">● www.palmerdepot.net</text>
  </g>
  <circle cx="175" cy="100" r="2.4" fill="#b3121b"/>
  <text x="180" y="102" font-family="Michroma, sans-serif" font-size="6.2" fill="#b3121b">PALMER DEPOT</text>
  <text x="211" y="110" font-family="Encode Sans Condensed, sans-serif" font-size="2.4" fill="#3c3c3c" text-anchor="middle">Oilfield • Plumbing • Industrial</text>
  <g transform="translate(191 205) rotate(-14)">
    <rect x="0" y="0" width="50" height="26" rx="1.5" fill="#fff"/>
    <text x="5" y="15" font-family="Michroma, sans-serif" font-size="2.4" fill="#b3121b">PALMER DEPOT</text>
    <text x="31" y="6" font-family="Encode Sans Condensed, sans-serif" font-size="1.8" fill="#b3121b">Marcus Palmer</text>
    <g font-family="Encode Sans Condensed, sans-serif" font-size="1.3" fill="#3c3c3c">
      <text x="31" y="10">555-304-1187</text><text x="31" y="12.5">555-304-2290</text><text x="31" y="15">555-304-3362</text><text x="31" y="17.5">marc@palmerdepot.net</text>
    </g>
  </g>
</svg>
<div class="label" style="left:1036px;top:253px">Folder</div>

</body>
</html>
```